KTR Football Academy Flyer

Flyer for a full page of a yearbook ( dimensions below ) along with all the contents/photos for the flyer.
Width - 210 mm
Height - 297 mm
Please also see attached the previous flyer which we feel is in need of an upgrade !
Flyer will also be used on social media pages.
Creating next level athletes !
Providing a platform and the correct environment for young football players to develop and fulfil their potential.
Why choose KTR Football Academy
- Multiple programs for everyone
- WAPL qualified & experienced coaches
- Safe and fun environment
- All coaches police checked
- Coaches Emergency First Aid Qualified
- Coaches Safeguarding Children Qualified
- Develop new skills
- Make new friends
- Improve your fitness
REGISTER NOW!
www.brightfieldathletix.example
+968 912 40637
Instagram/Facebook - ktrfootballacademy

```html
<!DOCTYPE html>
<html lang="en">
<head>
<meta charset="utf-8">
<title>KTR Football Academy Flyer</title>
<link rel="stylesheet" href="https://fonts.googleapis.com/css2?family=Montserrat:ital,wght@0,800;0,900;1,800&family=Lexend:wght@300;400;500&family=Oswald:wght@500&display=swap">
<style>
  :root {
    --green: #6cbd45;
    --green-kit: #2e9a57;
    --ink: #2b2b2b;
    --grey-panel: #e6e8ea;
    --page-bg: #d1d1d1;
    --paper: #ffffff;
  }
  * { margin: 0; padding: 0; box-sizing: border-box; }
  html, body { width: 1200px; height: 2400px; overflow: hidden; }
  body { background: var(--page-bg); position: relative; font-family: 'Lexend', sans-serif; color: var(--ink); }

  .flyer {
    position: absolute; left: 40px; top: 408px;
    width: 1120px; height: 1584px;
    background: var(--paper); overflow: hidden;
  }
  .flyer > * { position: absolute; }

  .halftone-wash {
    left: 0; top: 0; width: 560px; height: 520px;
    background: radial-gradient(ellipse at 0 0, #ececec 0%, rgba(255,255,255,0) 70%);
  }

  .side-bands { left: 0; top: 0; width: 1120px; height: 1584px; }

  .brand-mark {
    left: 850px; top: 150px; width: 170px;
    display: flex; align-items: center; gap: 12px;
    font-family: 'Montserrat', sans-serif; font-weight: 800;
    font-size: 54px; color: #fff; letter-spacing: 1px;
  }
  .brand-mark .dot { width: 30px; height: 30px; border-radius: 50%; background: #fff; flex: none; }

  .headline { left: 40px; top: 130px; width: 680px; font-family: 'Montserrat', sans-serif; font-weight: 900; text-align: center; }
  .headline .line-top { display: block; font-size: 80px; line-height: 1; letter-spacing: 1px; padding-left: 40px; }
  .headline .line-banner { display: block; position: relative; height: 116px; margin-top: -8px; }
  .headline .line-banner svg { position: absolute; left: 60px; top: 0; }
  .headline .line-banner span {
    position: relative; display: block; font-style: italic; font-weight: 800;
    font-size: 82px; color: #fff; line-height: 116px; padding-left: 40px;
  }
  .headline .line-bottom { display: block; font-size: 112px; line-height: 1; margin-top: -14px; letter-spacing: 1px; }

  .rule { left: 237px; top: 455px; width: 278px; height: 4px; background: var(--green); }

  .tagline { left: 40px; top: 484px; width: 700px; text-align: center; font-size: 28px; font-weight: 300; line-height: 41px; }
  .tagline strong { color: var(--green); font-weight: 500; }

  .snapshot { background: #fff; padding: 10px 10px 26px; box-shadow: 0 8px 18px rgba(0,0,0,.22); }
  .snapshot .photo { width: 100%; height: 100%; }
  .snapshot-1 { left: 5px; top: 630px; width: 248px; height: 240px; transform: rotate(-4deg); }
  .snapshot-2 { left: 256px; top: 700px; width: 160px; height: 216px; transform: rotate(4deg); }
  .snapshot-3 { left: 424px; top: 664px; width: 226px; height: 226px; transform: rotate(-4deg); }
  .snapshot-4 { left: 632px; top: 690px; width: 148px; height: 242px; transform: rotate(4deg); }
  .snapshot-5 { left: 482px; top: 1190px; width: 196px; height: 222px; transform: rotate(-6deg); }
  .tone-team { background: linear-gradient(180deg, #e4e6e8 0%, #d9dcdf 22%, #2f7d3e 40%, #2a6f38 68%, #7d9a55 82%, #6f8f4a 100%); }
  .tone-trophy { background: linear-gradient(180deg, #c9d3da 0%, #b7c3cc 25%, #2e4d3c 45%, #1f5a37 70%, #4c6f45 100%); }
  .tone-medal { background: linear-gradient(180deg, #ececec 0%, #e2e2e2 25%, #2c7b3f 45%, #2a6e3a 72%, #bfc6bd 100%); }
  .tone-hall { background: linear-gradient(180deg, #9fb3c6 0%, #d9dee2 30%, #3a8a49 50%, #3b7f46 70%, #d2d2cc 100%); }
  .tone-match { background: linear-gradient(180deg, #3b4a3d 0%, #566b54 28%, #3f8a46 50%, #9a86b4 64%, #5f8f49 100%); }

  .why-panel {
    left: 0; top: 965px; width: 779px; height: 230px;
    background: var(--grey-panel);
    border-top: 5px solid var(--green); border-bottom: 5px solid var(--green);
  }
  .why-panel h2 { position: absolute; left: 136px; top: 22px; font-size: 30px; font-weight: 500; white-space: nowrap; }
  .why-list { position: absolute; top: 72px; list-style: none; font-size: 17px; font-weight: 300; line-height: 27.5px; white-space: nowrap; }
  .why-list li { position: relative; padding-left: 22px; }
  .why-list li::before { content: "\2713"; position: absolute; left: 0; color: var(--green); font-weight: 500; }
  .why-list li.cont::before { content: ""; }
  .why-list-left { left: 88px; }
  .why-list-right { left: 452px; }

  .register { left: 0; top: 1248px; width: 448px; height: 92px; }
  .register span {
    position: absolute; left: 0; top: 0; width: 440px; height: 86px;
    display: flex; align-items: center; justify-content: center;
    font-family: 'Oswald', sans-serif; font-weight: 500; font-size: 56px; color: #fff; letter-spacing: 1px;
  }

  .contact { left: 90px; display: flex; align-items: center; gap: 14px; font-size: 25px; font-weight: 400; white-space: nowrap; }
  .contact-phone { top: 1376px; }
  .contact-web { top: 1430px; }
  .contact-social { top: 1496px; font-size: 14px; gap: 10px; }
  .contact-social .dot { width: 26px; height: 26px; border-radius: 50%; background: var(--green); }

  .player-photo {
    left: 800px; top: 690px; width: 300px; height: 820px;
    border-radius: 150px 150px 120px 120px / 200px 200px 120px 120px;
    background: linear-gradient(180deg, #33403a 0%, #33403a 7%, var(--green-kit) 12%, #27864b 50%, #f3f3f3 62%, #e6e6e6 90%, #555 100%);
  }
  .ball-photo {
    left: 640px; top: 1405px; width: 128px; height: 128px; border-radius: 50%;
    background: radial-gradient(circle at 40% 35%, #f6f6f6 0%, #c6d94a 60%, #4f9a46 100%);
  }
</style>
</head>
<body>
<main class="flyer">
  <div class="halftone-wash"></div>

  <svg class="side-bands" viewBox="0 0 1120 1584" aria-hidden="true">
    <polygon points="779,0 797,0 797,1000 457,1584 439,1584 779,1000" fill="#6cbd45"/>
    <polygon points="817,0 1046,0 1046,1000 706,1584 477,1584 817,1000" fill="#6cbd45"/>
    <polygon points="1067,0 1085,0 1085,1000 745,1584 727,1584 1067,1000" fill="#6cbd45"/>
  </svg>

  <div class="brand-mark"><span class="dot"></span><span>KTR</span></div>

  <h1 class="headline">
    <span class="line-top">CREATING</span>
    <span class="line-banner">
      <svg width="590" height="116" viewBox="0 0 590 116" aria-hidden="true"><polygon points="30,22 590,0 570,96 0,116" fill="#6cbd45"/></svg>
      <span>NEXT LEVEL</span>
    </span>
    <span class="line-bottom">ATHLETES</span>
  </h1>

  <div class="rule"></div>

  <p class="tagline">Providing a platform and the correct environment<br>for <strong>young football</strong> players to develop and<br><strong>fulfil their potential</strong></p>

  <figure class="snapshot snapshot-1"><div class="photo tone-team" role="img" aria-label="Girls team in green kit posing on the pitch"></div></figure>
  <figure class="snapshot snapshot-2"><div class="photo tone-trophy" role="img" aria-label="Young players holding a framed award"></div></figure>
  <figure class="snapshot snapshot-3"><div class="photo tone-medal" role="img" aria-label="Boys team with medals at a tournament"></div></figure>
  <figure class="snapshot snapshot-4"><div class="photo tone-hall" role="img" aria-label="Two young players in an indoor hall"></div></figure>

  <section class="why-panel">
    <h2>Why choose KTR Football Academy :</h2>
    <ul class="why-list why-list-left">
      <li>Multiple programs for everyone</li>
      <li>WAPL qualified &amp; experienced coaches</li>
      <li>Safe and fun environment</li>
      <li>All coaches police checked</li>
      <li>Coaches Emergency First Aid Qualified</li>
    </ul>
    <ul class="why-list why-list-right">
      <li>Coaches Safeguarding</li>
      <li class="cont">Children Qualified</li>
      <li>Develop new skills</li>
      <li>Make new friends</li>
      <li>Improve your fitness</li>
    </ul>
  </section>

  <div class="register">
    <svg width="448" height="92" viewBox="0 0 448 92" aria-hidden="true">
      <path d="M0,6 H420 Q448,6 448,34 V70 Q448,92 424,92 H0 Z" fill="#d9d9d9"/>
      <path d="M0,0 H412 Q440,0 440,28 V62 Q440,86 416,86 H0 Z" fill="#6cbd45"/>
    </svg>
    <span>REGISTER NOW</span>
  </div>

  <figure class="snapshot snapshot-5"><div class="photo tone-match" role="img" aria-label="Match action between two young players"></div></figure>

  <div class="contact contact-phone">
    <svg width="36" height="36" viewBox="0 0 36 36" aria-hidden="true"><circle cx="18" cy="18" r="16" fill="none" stroke="#6cbd45" stroke-width="2.5"/><path d="M12 10 L15 10 L16.5 14 L14.5 15.5 Q16 19.5 20.5 21.5 L22 19.5 L26 21 L26 24 Q25 26 22.5 26 Q11 24 10 12.5 Q10 10 12 10 Z" fill="none" stroke="#6cbd45" stroke-width="2" stroke-linejoin="round"/></svg>
    <span>+968 912 40637</span>
  </div>
  <div class="contact contact-web">
    <svg width="36" height="36" viewBox="0 0 36 36" aria-hidden="true"><g fill="none" stroke="#6cbd45" stroke-width="2.5"><circle cx="18" cy="18" r="16"/><ellipse cx="18" cy="18" rx="7" ry="16"/><line x1="2" y1="18" x2="34" y2="18"/><line x1="5" y1="10" x2="31" y2="10"/><line x1="5" y1="26" x2="31" y2="26"/></g></svg>
    <span>www.brightfieldathletix.example</span>
  </div>
  <div class="contact contact-social">
    <span class="dot"></span>
    <span>ktrfootballacademy</span>
  </div>

  <div class="player-photo" role="img" aria-label="Young academy player in green kit striking a football"></div>
  <div class="ball-photo" role="img" aria-label="Football at the player's feet"></div>
</main>
</body>
</html>
```